Verpackungsdesign für italienische Produkte gesucht
Die Zusammenarbeit mit dem Designer 7Pixo hat sehr viel Spaß gemacht. Jeder Änderungswunsch wurde super schnell in die Tat umgesetzt. Die Kommunikation verlief reibungslos. Das Ergebnis ist einfach klasse geworden. Er hat ein großes Talent für den Entwurf von Designs. Ich freue mich sehr darauf, auch zukünftige Projekte mit ihm durchführen zu können. Vielen Dank nochmal an Ihn für die tolle Arbeit und die Unterstützung. Ich kann eine Zusammenabeit mit dem Designer 7Pixo nur empfehlen.
Liebe Designerinnen und Designer,
wir sind ein Unternehmen, welches Olivenöl, Pasta und Wein sowie Olivenblättertee und Tomatensoße auf Sizilien (Italien) in Gibellina produziert. In vierter Generation produziert die Familie Berardi landwirtschaftliche Erzeugnisse, die nach biologischen Prinzipien angebaut werden. Im Ackerbau verzichten wir auf synthetisch hergestellte Pflanzenschutzmittel, Mineraldünger und Grüne Gentechnik. Da in der heutigen Zeit viele Konsumenten den Ursprung der gekauften Produkte nicht mehr zurückverfolgen können und ihnen in dieser Hinsicht kaum Transparenz gewährleistet wird, möchten wir im Namen der Familie Berardi unseren Kunden den Herstellungsprozess vom Anbau bis zur Fertigstellung des Enderzeugnisses transparent aufzeigen und sie für die bewusste und gesunde Ernährung sensibilisieren.
Unsere Zielgruppe sind ernährungsbewusste Personen, überwiegend Frauen im mittleren Alter, die auf bewusste, gesunde Ernährung viel Wert legen.
Vielen lieben Dank für eure Arbeit im Voraus. Ich freue mich sehr auf die Designvorschläge.
Lieben Gruß
Marta & Lorenzo Berardi
KREATIVE DESIGNER gesucht
WIR SUCHEN EIN VERPACKUNGSKONZEPT FÜR UNSERE PRODUKTE
Für unsere Produkte: Olivenöl, Pasta und Wein sowie Olivenblättertee und Tomatensoße benötigen wir ein Verpackungsdesign, welches erkennen lässt, dass die Produkte zu einer Produktfamilie gehören. Darüber hinaus benötigen wir das Design für den Kartonanhänger, der an jedes unserer Produkte ran gehängt werden soll.
Erst einmal suchen wir nach Vorschlägen für ein Verpackungsdesign. Im Anschluss an dieses Projekt würden wir gerne mit dem Designer die Reinzeichnungen fertig erstellen. Den Preis für die Reinzeichnung würden wir dann gerne mit dem Designer verhandeln.
Mit dem Designer, der das Projekt gewinnt, streben wir auch nach dem Produktende eine enge Zusammenarbeit an, da sich unser Produktportfolio stetig erweitern wird und Folgeaufträge bereits in Planung sind.
Für die Produkte Olivenöl, Pasta und Tee sowie Tomatensoße benötigen wir Etiketten mit Vorder- und Rückseite. Für die Pasta-Verpackung soll ein Design für den Kartonreiter aus dünnem Kartonpapier erstellt werden (siehe Bild Pasta Design Beispiel). Dieses Kartonpapier könnte schwarz sein, da die Olivenölflasche, die Weinflaschen sowie die Verpackung für Tee und die Flasche für Tomatensoße ebenfalls dunkel sind.
Das Design sollte elegant und qualitativ hochwertig aussehen. Mit unseren Produkten sollen die folgenden Werte transportiert werden: Tradition, Familie, hochwertige Qualität, Transparenz, biologischer Anbau, bewusste Ernährung, Liebe zum Produkt, Sizilien,
Es sollten max. 4 verschiedene Farben verwendet werden.
In der Datei Vorgaben zum Design stehen weitere Angaben. Zusätzlich besteht eine PDF Datei mit Bildern zur Gestaltungshilfe. Eine weitere Datei besteht mit allen Verpackungen, die gestaltet werden sollen.
Alle Logos sind auch noch in weiteren Formaten verfügbar.
Vielen Dank im Voraus
Marta & ..

```html
<!DOCTYPE html>
<html lang="de">
<head>
<meta charset="utf-8">
<title>Berardi – Tagliatelle Kartonreiter</title>
<link rel="stylesheet" href="https://fonts.googleapis.com/css2?family=Merriweather:wght@400;700;900&display=swap">
<style>
  :root {
    --page: #ffffff;
    --card: #1e1e1e;
    --band: #2a2a2a;
    --band-light: #333333;
    --gold: #c9a227;
    --gold-light: #f2e38a;
    --gold-dark: #8a5a1e;
    --white: #ffffff;
    --grey: #bdbdbd;
    --grey-dark: #9a9a9a;
    --icon: #bfbfbf;
    --organic: #8fbe24;
    --pasta-light: #fde58a;
    --pasta: #f3c238;
    --pasta-dark: #e0a21c;
  }
  * { margin: 0; padding: 0; box-sizing: border-box; }
  html, body { width: 1200px; height: 1200px; overflow: hidden; background: var(--page); }
  body { position: relative; font-family: "Merriweather", Georgia, serif; }

  .label {
    position: absolute; left: 229px; top: 48px; width: 749px; height: 1111px;
    background: var(--card);
  }
  .label > * { position: absolute; }

  .organic-badge { left: 597px; top: 34px; width: 116px; height: 65px; background: var(--organic); }
  .organic-note { left: 570px; top: 107px; width: 170px; text-align: center; font-size: 16px; color: var(--grey); }

  .brand-name {
    left: 0; top: 140px; width: 749px; text-align: center;
    font-size: 34px; font-weight: 700; color: var(--white); line-height: 44px;
  }

  .title-band {
    left: 0; top: 316px; width: 749px; height: 254px;
    background: radial-gradient(ellipse at 50% 50%, var(--band-light), var(--band) 70%);
  }
  .title-rule { left: 108px; width: 534px; height: 3px; background: var(--white); }
  .title-rule.top { top: 344px; }
  .title-rule.bottom { top: 474px; }
  .product-name {
    left: 0; top: 364px; width: 749px; text-align: center;
    font-size: 68px; font-weight: 900; color: var(--white); letter-spacing: 5px; line-height: 96px;
  }

  .claim-icon { top: 496px; width: 56px; height: 56px; }
  .claim-icon.mill { left: 237px; }
  .claim-icon.dna { left: 346px; }
  .claim-icon.additive { left: 455px; }

  .info-frame {
    left: 56px; top: 746px; width: 638px; height: 245px;
    border: 7px solid transparent;
    border-image: linear-gradient(90deg, var(--gold), var(--gold-light) 50%, var(--gold-dark)) 1;
  }
  .pasta-photo {
    left: 263px; top: 632px; width: 233px; height: 194px;
    border-radius: 48% 52% 40% 45% / 50% 55% 45% 50%;
    background: radial-gradient(ellipse at 40% 40%, var(--pasta-light), var(--pasta) 55%, var(--pasta-dark));
  }
  .product-type {
    left: 0; top: 862px; width: 749px; text-align: center;
    font-size: 23px; font-weight: 700; color: var(--white); line-height: 32px;
  }
  .product-facts {
    left: 0; top: 904px; width: 749px; text-align: center;
    font-size: 16px; color: var(--white); line-height: 26px;
  }

  .net-weight { left: 95px; top: 1033px; font-size: 25px; font-weight: 700; color: var(--white); }
  .social { right: 72px; top: 1040px; display: flex; align-items: center; gap: 10px; font-size: 15px; color: var(--grey-dark); }
  .social .channel { color: var(--grey); }
</style>
</head>
<body>
  <main class="label">
    <div class="organic-badge" role="img" aria-label="Bio-Siegel"></div>
    <p class="organic-note">100 % Natürlich</p>

    <p class="brand-name">Berardi</p>

    <div class="title-band" role="img" aria-label="Dunkles Hintergrundbild mit Weizenähren"></div>
    <div class="title-rule top"></div>
    <h1 class="product-name">TAGLIATELLE</h1>
    <div class="title-rule bottom"></div>

    <svg class="claim-icon mill" viewBox="0 0 56 56" fill="none" stroke="var(--icon)" stroke-width="1.5" aria-label="Steinmühle">
      <path d="M18 54V36l10-8 10 8v18z"/>
      <path d="M14 18l28 28M42 18L14 46"/>
      <circle cx="28" cy="32" r="2"/>
      <path d="M22 48h12M28 44v4"/>
      <path d="M6 6l44 44"/>
    </svg>
    <svg class="claim-icon dna" viewBox="0 0 56 56" fill="none" stroke="var(--icon)" stroke-width="1.5" aria-label="Ohne Gentechnik">
      <path d="M4 46c12-4 12-28 24-20s12-16 24-20"/>
      <path d="M4 38c12 12 16-12 24-4s12-16 24-22"/>
      <path d="M14 40v-8M22 34v-8M34 28v-8M42 20v-8"/>
      <path d="M14 14l32 32"/>
    </svg>
    <svg class="claim-icon additive" viewBox="0 0 56 56" fill="none" stroke="var(--icon)" stroke-width="1.5" aria-label="Ohne Zusatzstoffe">
      <path d="M36 8l12 12-6 6-12-12z"/>
      <path d="M32 20L10 42l-2 6 6-2 22-22"/>
      <path d="M10 12l36 36"/>
    </svg>

    <div class="info-frame"></div>
    <div class="pasta-photo" role="img" aria-label="Foto von Tagliatelle-Nestern"></div>
    <h2 class="product-type">Bio-Vollkornpasta mit Weizenkeimen</h2>
    <p class="product-facts">100 % Hartweizen aus Sizilien<br>100 % Mehl aus Steinmühle</p>

    <p class="net-weight">500 g</p>
    <p class="social">Folgen Sie uns auf: <span class="channel">Pinnwand</span> <span class="channel">Bildstrom</span></p>
  </main>
</body>
</html>
```